Tidewell Consulting Schedule Of Rates

We need a brochure / proposal for our new company. Our company is a start up based in Australia who provides engineering and sales support to other renewable energy companies. Our brochure is a pitch-deck / sales item that catalogues our key services. We are engineering consultants.

Our website is www.tidewellpartners.com.au. Please review the website to get a feel of colour schemes etc.

We are looking for a strong, trustworthy feel, but the brochure also needs to be sales driven and to the point.

The second page that contains the $30 price point needs to be loud and clear.

The use of relevant icons throughout the document will be viewed favorably.

Please format the tables to look attractive.

The document will need to be in an editable format so content can be edited by us at a later date.

Please feel free to use the pics within the attached word document. The winning design will be provided with updated, clearer images upon request.

Thank you

Target Market(s)

Businesses that either sell or install solar PV and other renewable energy systems in Australia. Most of target market are likely to be electrical contractors.

Industry/Entity Type

Engineering

Colors
0255a3
0492cd
ffffff

Requirements
Must have
• Icons, graphics presentation, Clean and Clear, Business oriented. Sharp sales feel
Nice to have
• solar picture backgrounds maybe
Should not have
• cartoons, over sales driven,

```html
<!DOCTYPE html>
<html lang="en">
<head>
<meta charset="utf-8">
<title>Tidewell Consulting – Professional Panel Layout</title>
<link href="https://fonts.googleapis.com/css2?family=Barlow:wght@400;600;700&display=swap" rel="stylesheet">
<style>
  :root {
    --brand-blue: #1a78cf;
    --brand-deep: #0255a3;
    --ink: #1d1d1f;
    --paper: #ffffff;
    --backdrop: #e9e7e3;
    --roof-light: #c9cbc8;
    --roof-dark: #8f948f;
    --site-light: #a9aea4;
    --site-dark: #5d655c;
  }
  * { box-sizing: border-box; margin: 0; padding: 0; }
  html, body {
    width: 1200px; height: 1200px; overflow: hidden;
    background: var(--backdrop);
    font-family: "Barlow", Arial, sans-serif;
  }
  .sheet {
    position: absolute; left: 160px; top: 30px;
    width: 880px; height: 1140px;
    background: var(--paper);
    box-shadow: 0 4px 18px rgba(0,0,0,0.12);
  }
  .brand {
    position: absolute; right: 49px; top: 58px;
    display: flex; align-items: center; gap: 10px;
    font-weight: 700; font-size: 30px; color: var(--ink);
    letter-spacing: -0.5px;
  }
  .brand-mark { width: 14px; height: 14px; background: var(--brand-blue); }
  .section-title {
    position: absolute; left: 48px; top: 118px;
    font-weight: 700; font-size: 34px; color: var(--brand-blue);
    letter-spacing: 0.5px; line-height: 1;
  }
  .section-subtitle {
    position: absolute; left: 48px; top: 160px;
    font-weight: 400; font-size: 36px; color: var(--brand-blue);
    letter-spacing: 0.5px; line-height: 1;
  }
  .section-rule {
    position: absolute; left: 48px; right: 49px; top: 201px;
    height: 2px; background: var(--brand-blue);
  }
  .features {
    position: absolute; left: 48px; top: 225px;
    display: grid; grid-template-columns: 415px auto; row-gap: 4px;
    list-style: none; font-size: 18.5px; color: var(--ink);
  }
  .features li::before { content: "•"; display: inline-block; width: 23px; }
  .features .range { grid-column: 2; grid-row: 1; }
  .offer {
    position: absolute; left: 49px; width: 782px; height: 387px;
    display: flex;
  }
  .offer-small { top: 300px; }
  .offer-large { top: 703px; }
  .offer-visual { width: 501px; height: 100%; }
  .offer-small .offer-visual { background: linear-gradient(160deg, var(--roof-light), var(--roof-dark)); }
  .offer-large .offer-visual { background: linear-gradient(120deg, var(--site-dark), var(--site-light) 55%, var(--site-dark)); }
  .offer-prices {
    flex: 1; background: var(--brand-blue); color: var(--paper);
    padding: 35px 0 0 41px; font-size: 19.5px; line-height: 1.3;
  }
  .tier { margin-bottom: 23px; }
  .tier-lead { font-weight: 600; }
  .tier-lead .tier-range { font-size: 19.5px; }
  .tier-price { display: block; font-size: 36px; font-weight: 700; line-height: 1.15; margin: 2px 0 1px; }
</style>
</head>
<body>
  <main class="sheet">
    <div class="brand"><span class="brand-mark"></span>Tidewell Consulting</div>

    <h1 class="section-title">SERVICES</h1>
    <h2 class="section-subtitle">PROFESSIONAL PANEL LAYOUT</h2>
    <div class="section-rule"></div>

    <ul class="features">
      <li>We can layout the panels for a small fee</li>
      <li class="range">Ranging from 5kW – 300kW</li>
      <li>Clear &amp; Concise</li>
    </ul>

    <section class="offer offer-small">
      <div class="offer-visual" role="img" aria-label="Aerial view of a warehouse roof with rows of solar panels laid out"></div>
      <div class="offer-prices">
        <div class="tier tier-lead">
          <span class="tier-range">Less then 30kW</span>
          <span class="tier-price">$30</span>
          Ex. Gst Skyplot<br>Panel Layout
        </div>
        <div class="tier">31kW - 100kW<br>$80 Ex. Gst Skyplot<br>Panel Layout</div>
        <div class="tier">101kW - 300kW<br>$150 Ex. Gst Skyplot<br>Panel Layout</div>
      </div>
    </section>

    <section class="offer offer-large">
      <div class="offer-visual" role="img" aria-label="Aerial 3D model of a large industrial roof with solar array beside a highway"></div>
      <div class="offer-prices">
        <div class="tier tier-lead">
          <span class="tier-range">300kW +</span>
          <span class="tier-price">$360</span>
          Ex. Gst<br>3D Drawing<br>including shading<br>analysis
        </div>
      </div>
    </section>
  </main>
</body>
</html>
```